professional business card design

Business card design. Photos have been uploaded and i am open to the designer choosing which photos to use. Would like the card to be mostyly in a grey scale design with black, whites, silver & grey colours. I have added copy of our flyer as would like on the back side of card our services to be listed. Do not use any bright colurs such as blue red green or yellow. i need to be able to edit the phone number and naem in the final card design submitted.

Target Market(s)

Clients

Industry/Entity Type

earhmovibng and transport

Contact Information for Business Card

Director Name, address, email, phone number and services

Colors

Designer to choose only greyscale colors for use in the design.

Requirements
Should not have
• no yellow, red, blue or green

```html
<!DOCTYPE html>
<html lang="en">
<head>
<meta charset="utf-8">
<title>KVR Pty Ltd – Business Card</title>
<link rel="stylesheet" href="https://fonts.googleapis.com/css2?family=Roboto:wght@400;500;700&family=Exo+2:wght@600;700;800&display=swap">
<style>
  :root{
    --bg:#8a8a8a;
    --card-dark:#0c0c0c;
    --card-dark-mid:#262626;
    --card-light:#d9d9d9;
    --ink:#2b2b2b;
    --ink-soft:#3a3a3a;
    --silver:#e6e6e6;
    --silver-dim:#b5b5b5;
    --photo-a:#3d3d3d;
    --photo-b:#1a1a1a;
    --photo-light-a:#5a5a5a;
    --photo-light-b:#2e2e2e;
  }
  *{box-sizing:border-box;margin:0;padding:0}
  html,body{width:1200px;height:1085px;overflow:hidden}
  body{background:var(--bg);position:relative;font-family:"Roboto",sans-serif}

  .card{position:absolute;width:620px;height:352px;border-radius:10px;overflow:hidden;box-shadow:0 6px 18px rgba(0,0,0,.35)}

  /* Back side – services */
  .card--services{left:290px;top:140px;background:
      radial-gradient(ellipse at 50% 35%, var(--card-dark-mid) 0%, var(--card-dark) 70%);}
  .card--services .brand{position:absolute;left:0;right:0;top:46px;text-align:center;
      font-family:"Exo 2",sans-serif;font-weight:800;font-size:56px;letter-spacing:2px;color:var(--silver);line-height:1}
  .card--services .brand-suffix{position:absolute;left:0;right:0;top:114px;text-align:center;
      font-family:"Exo 2",sans-serif;font-weight:700;font-size:15px;color:var(--silver-dim)}
  .card--services .fleet-photo{position:absolute;left:0;right:0;top:160px;height:82px;
      background:linear-gradient(180deg,var(--photo-a) 0%,var(--photo-b) 100%)}
  .services-title{position:absolute;left:30px;top:244px;font-family:"Exo 2",sans-serif;font-weight:700;
      font-size:18px;letter-spacing:1px;color:var(--silver);text-transform:uppercase;line-height:1.2}
  .services-list{position:absolute;left:30px;top:272px;width:575px;list-style:none;
      display:grid;grid-template-columns:220px 1fr;row-gap:2px;
      font-family:"Exo 2",sans-serif;font-weight:700;font-size:10px;font-variant:small-caps;
      color:var(--silver);letter-spacing:.6px;line-height:11px}
  .services-list li{display:flex;align-items:center;gap:5px;white-space:nowrap}
  .services-list li::before{content:"";width:6px;height:6px;border:1.5px solid var(--silver);flex:none}
  .services-list .wide{grid-column:1 / 3}

  /* Front side – contact */
  .card--contact{left:290px;top:580px;background:var(--card-light)}
  .person-name{position:absolute;left:46px;top:52px;font-weight:700;font-size:25px;color:var(--ink);letter-spacing:.3px;line-height:1.2}
  .person-role{position:absolute;left:46px;top:84px;font-weight:500;font-size:12.5px;color:var(--ink-soft);letter-spacing:.3px;line-height:1.2}
  .role-rule{position:absolute;left:232px;right:46px;top:92px;height:2px;background:var(--ink-soft)}
  .card--contact .brand{position:absolute;right:46px;top:50px;font-weight:700;font-size:26px;color:var(--ink);letter-spacing:1px;line-height:1.2}
  .card--contact .fleet-photo{position:absolute;left:16px;right:6px;top:126px;height:118px;
      background:linear-gradient(90deg,var(--photo-light-a) 0%,var(--photo-light-b) 100%);border-radius:4px}
  .contact-line{position:absolute;font-size:16px;line-height:20px;color:var(--ink-soft);letter-spacing:.2px;white-space:nowrap}
  .contact-phone{right:46px;top:252px}
  .contact-email{right:46px;top:276px}
  .contact-web{right:46px;top:301px}
  .contact-address{left:46px;top:301px}
</style>
</head>
<body>

<section class="card card--services" aria-label="Card back – services">
  <div class="brand">KVR</div>
  <div class="brand-suffix">Pty Ltd</div>
  <div class="fleet-photo" role="img" aria-label="Photo of road train side tipper trailers on a dirt road"></div>
  <h2 class="services-title">Our Services</h2>
  <ul class="services-list">
    <li>Over size loads/ Hot Shot Loads</li>
    <li>Heavy Vehicle Recovery Services</li>
    <li>Potable Water Deliveries</li>
    <li>Road Building / Maintenance</li>
    <li>Sand &amp; Metal Supply &amp; Cartage:</li>
    <li>Road Train Tippers</li>
    <li>Road Train Tankers</li>
    <li>Road Train Flat Tops</li>
    <li class="wide">Mine Site accredited equipment &amp; Operators</li>
  </ul>
</section>

<section class="card card--contact" aria-label="Card front – contact">
  <h1 class="person-name">MARCUS HALE</h1>
  <p class="person-role">GRAPHIC DESIGNER &amp; CEO</p>
  <div class="role-rule"></div>
  <div class="brand">KVR</div>
  <div class="fleet-photo" role="img" aria-label="Photo of a road train truck pulling three side tipper trailers"></div>
  <p class="contact-line contact-phone">0098 7654 32100</p>
  <p class="contact-line contact-email">hello@kvrhaulage.com</p>
  <p class="contact-line contact-web">kvrhaulage.com</p>
  <p class="contact-line contact-address">45 Depot Road, Kalgoorlie</p>
</section>

</body>
</html>
```